Designing a website for Brightmoor Pest Services PTY LTD

Pest control company looking for someone to build an informative website containing services we offer and an online inquiry form.
Commercial premises - Specialising in - Rodent control, stored product pest control, flying insect control, ant, spider and insect control, Termite inspections and treatments. Termite management systems on a commercial scale.
Facilities we service
Commercial - shopping centres, transport facilities, restaurants, pubs, clubs, bars food manufacturing facilities.
Residential - Houses specialising in - Rodent, Ant, Spider, Cockroach and Termite control. Termite inspections, Pre - purchase inspections, Termite treatments, Termite management systems.
Target Market(s)
Mainly commercial and industrial clients and Residential clients.
Industry/Entity Type
Pest Control
Number of Pages Required
1 page
Look and feel

```html
<!DOCTYPE html>
<html lang="en">
<head>
<meta charset="utf-8">
<title>Brightmoor Pest Services PTY LTD</title>
<link href="https://fonts.googleapis.com/css2?family=Sen:wght@400;700;800&display=swap" rel="stylesheet">
<style>
:root{
  --backdrop:#7aa8ad;
  --page:#f5f6fb;
  --teal:#1d5a64;
  --teal-dark:#0f3f4a;
  --green:#4ee59b;
  --green-soft:#dff3e8;
  --ink:#1a2e3a;
  --muted:#5b6b74;
  --navy:#0f1535;
  --white:#ffffff;
  --line:#d7dde3;
}
*{box-sizing:border-box;margin:0;padding:0}
html,body{width:1200px;height:4024px;overflow:hidden}
body{background:var(--backdrop);font-family:"Sen",sans-serif;color:var(--ink);position:relative}
.page{position:absolute;left:227px;top:147px;width:746px;height:3730px;background:var(--page);overflow:hidden}
.abs{position:absolute}
.photo{position:absolute}
.tag{position:absolute;height:16px;padding:0 9px;font-size:7px;line-height:16px;background:var(--green-soft);color:var(--teal);border-radius:2px;white-space:nowrap}
.btn{position:absolute;display:flex;align-items:center;justify-content:center;font-size:10px;color:var(--white);background:var(--teal);border-radius:2px}
.h-sec{position:absolute;left:0;width:746px;text-align:center;font-size:12.5px;font-weight:700;color:var(--teal-dark);line-height:16px}
.small{font-size:6.5px;line-height:10px;color:var(--muted)}

/* nav + hero */
.hero{left:0;top:0;width:746px;height:420px;background:linear-gradient(110deg,#1f4a55 0%,#3d6b73 45%,#8ea6ad 75%,#c7d2d6 100%)}
.nav{left:0;top:0;width:746px;height:37px;border-bottom:1px solid rgba(255,255,255,.25)}
.nav .logo{position:absolute;left:56px;top:13px;font-size:8.5px;font-weight:700;color:var(--green)}
.nav ul{list-style:none;position:absolute;top:14px;left:0;width:746px}
.nav li{position:absolute;font-size:7px;color:var(--white)}
.nav li.on{color:var(--green)}
.nav li.on::after{content:"";position:absolute;left:-6px;right:-6px;top:20px;height:2px;background:var(--green)}
.nav .cta{position:absolute;left:632px;top:10px;width:56px;height:17px;background:var(--green);color:var(--teal-dark);font-size:6.5px;display:flex;align-items:center;justify-content:center;border-radius:2px}
.hero-tag{left:56px;top:106px;background:rgba(255,255,255,.35);color:var(--white)}
.hero h1{position:absolute;left:56px;top:134px;font-size:31px;line-height:36.5px;font-weight:400;color:var(--white)}
.hero h1 span{color:var(--green);font-weight:700}
.hero .btn{left:56px;top:300px;width:92px;height:30px;background:var(--green);color:var(--teal-dark)}
.arrow{position:absolute;left:668px;width:20px;height:20px;border:1px solid var(--white);border-radius:50%}

/* about */
.about-photo{left:56px;top:523px;width:281px;height:225px;background:linear-gradient(135deg,#6b4a32,#a9876a 50%,#e3dcd4)}
.about-note{left:50px;top:705px;width:128px;height:50px;background:var(--green-soft);padding:9px 6px;font-size:5.5px;line-height:8px;color:var(--teal)}
.about h2{position:absolute;left:398px;top:541px;width:300px;font-size:11.5px;line-height:15px;color:var(--teal-dark)}
.about p{position:absolute;left:398px;top:588px;width:290px}
.about .btn{left:398px;top:705px;width:91px;height:30px}

/* why */
.feature{position:absolute;left:56px;width:259px;height:77px;padding:12px 12px 0 46px}
.feature.card{background:var(--white);box-shadow:0 4px 14px rgba(20,50,60,.08)}
.feature h3{font-size:8px;font-weight:400;color:var(--teal-dark);margin-bottom:5px}
.feature .ic{position:absolute;left:12px;top:11px;width:20px;height:20px;border-radius:50%;background:var(--teal)}
.why-photo{left:420px;top:978px;width:270px;height:208px;background:linear-gradient(135deg,#2f3739,#7f8a8c 45%,#e4e7e8)}

/* services */
.srv h2{position:absolute;left:520px;top:1372px;width:180px;font-size:11.5px;line-height:15px;color:var(--teal-dark)}
.svc{position:absolute;width:194px;height:241px;background:var(--white);box-shadow:0 4px 14px rgba(20,50,60,.08);text-align:center}
.svc svg{position:absolute;left:52px;top:32px}
.svc h3{position:absolute;top:162px;left:0;width:194px;font-size:8px;font-weight:400;color:var(--teal)}
.svc p{position:absolute;top:180px;left:16px;width:162px}

/* facilities */
.fac{position:absolute;left:56px;width:634px;height:294px;background:var(--white);box-shadow:0 4px 14px rgba(20,50,60,.08)}
.fac .photo{top:0;width:317px;height:294px}
.fac .body{position:absolute;top:26px;width:270px}
.fac h3{font-size:16px;font-weight:700;color:var(--teal);margin:8px 0 4px}
.fac ul{list-style:none;display:grid;grid-template-columns:105px 140px;gap:4px 0;margin-top:12px}
.fac li{font-size:6px;color:var(--ink);display:flex;align-items:center;gap:4px}
.fac li::before{content:"";width:6px;height:6px;border:1px solid var(--teal);border-radius:50%}
.fac .btn{position:relative;margin-top:24px;width:91px;height:30px}

/* stats */
.stats{left:0;top:2920px;width:746px;height:206px;background:linear-gradient(180deg,#15535f,#0f3f4a)}
.stats h2{position:absolute;left:127px;top:42px;font-size:16px;line-height:23px;color:var(--white)}
.stat{position:absolute;top:42px;color:var(--white)}
.stat b{display:block;font-size:19px}
.stat span{font-size:6px}
.stats p{position:absolute;left:336px;top:94px;width:330px;color:#c7d8dc}

/* contact */
.contact{left:83px;top:3077px;width:581px;height:342px;background:var(--white);box-shadow:0 6px 20px rgba(20,50,60,.12)}
.appt{left:0;top:0;width:250px;height:342px;background:linear-gradient(160deg,#2c6d75,#1b535d)}
.appt .frame{position:absolute;left:10px;top:12px;width:230px;height:318px;border:1px solid rgba(255,255,255,.3)}
.appt h3{position:absolute;left:46px;top:148px;font-size:16px;line-height:22px;color:var(--white)}
.appt p{position:absolute;left:46px;top:199px;width:150px;color:#d6e6e8}
.contact h2{position:absolute;left:300px;top:37px;font-size:14px;color:var(--ink)}
.field{position:absolute;left:300px;width:228px;height:28px;border:1px solid var(--line);font-size:6px;color:#9aa5ad;padding:10px 12px}
.field svg{position:absolute;right:10px;top:9px}
.send{position:absolute;left:300px;top:267px;width:228px;height:30px;background:linear-gradient(180deg,#1f6671,#134752);color:var(--white);font-size:9px;display:flex;align-items:center;justify-content:center}

/* footer */
.footer{left:0;top:3495px;width:746px;height:235px;background:var(--navy)}
.footer .brand{position:absolute;left:98px;top:50px;font-size:10.5px;font-weight:700;color:var(--green)}
.footer .about{position:absolute;left:98px;top:72px;width:130px;font-size:5.5px;line-height:8.5px;color:#b8bfd0}
.footer ul{list-style:none;position:absolute;left:365px;top:50px}
.footer li{font-size:6.5px;color:#d5d9e5;margin-bottom:13px}
.footer li.on{color:var(--green)}
.footer .ct{position:absolute;left:525px;top:50px;font-size:6.5px;color:var(--white)}
.crow{position:absolute;left:525px;display:flex;gap:10px;align-items:flex-start;font-size:5.5px;line-height:8px;color:#d5d9e5}
.crow i{flex:none;width:14px;height:14px;border-radius:50%;background:#262d52;display:flex;align-items:center;justify-content:center}
.copy{position:absolute;left:0;bottom:0;width:746px;height:22px;border-top:1px solid #262d52;font-size:6px;color:#d5d9e5;text-align:center;line-height:22px}
</style>
</head>
<body>
<main class="page">

  <header class="abs hero">
    <div class="photo" style="inset:0" role="img" aria-label="Technician in white protective suit and respirator spraying a garden"></div>
    <nav class="abs nav">
      <div class="logo">Brightmoor Pest Services PTY LTD</div>
      <ul>
        <li class="on" style="left:317px">Home</li>
        <li style="left:358px">About Us</li>
        <li style="left:410px">Services</li>
        <li style="left:459px">Facilities</li>
        <li style="left:510px">Commercial</li>
        <li style="left:571px">Residential</li>
      </ul>
      <div class="cta">Contact Us</div>
    </nav>
    <div class="tag hero-tag">Lorem ipsum dolor sit amet, consetetur sadipscing elitr, sed diam</div>
    <h1>Highly Expert<br><span>Pest Control</span><br>Solution &amp;<br>Company</h1>
    <div class="btn">Contact Now</div>
    <div class="arrow" style="top:194px"><svg width="18" height="18" viewBox="0 0 18 18"><path d="M5 9h8M10 6l3 3-3 3" stroke="#fff" fill="none"/></svg></div>
    <div class="arrow" style="top:225px"><svg width="18" height="18" viewBox="0 0 18 18"><path d="M13 9H5M8 6 5 9l3 3" stroke="#fff" fill="none"/></svg></div>
  </header>

  <section class="about">
    <div class="photo about-photo" role="img" aria-label="Smiling technician spraying kitchen cabinets"></div>
    <div class="abs about-note">Lorem ipsum dolor sit amet, consetetur sadipscing elitr, sed diam nonumy eirmod tempor invidunt ut labore et</div>
    <h2>We are Highly Expert in Pest Control Solution sadipscing elitr, sed diam nonumy</h2>
    <p class="small">Lorem ipsum dolor sit amet, consetetur sadipscing elitr, sed diam nonumy eirmod tempor invidunt ut labore et dolore magna aliquyam erat, sed diam voluptua. At vero eos et accusam et justo duo dolores et ea rebum. Stet clita kasd gubergren, no sea takimata sanctus est Lorem ipsum dolor sit amet. Lorem ipsum dolor sit amet, consetetur sadipscing elitr, sed diam nonumy eirmod tempor invidunt ut labore et dolore magna aliquyam erat, sed diam voluptua. At vero eos et accusam et justo duo dolores et ea rebum. Stet clita kasd gubergren, no sea takimata sanctus est Lorem ipsum dolor sit amet.</p>
    <div class="btn">Know More</div>
  </section>

  <section class="why">
    <div class="tag" style="left:346px;top:867px">Why choose us</div>
    <h2 class="h-sec" style="top:898px">Lorem ipsum dolor sit amet, consetetur sadipscing elitr,<br>sed diam nonumy</h2>
    <div class="feature card" style="top:966px"><span class="ic"></span><h3>Save Your Time And Money</h3><p class="small">Lorem ipsum dolor sit amet, consetetur sadipscing elitr, sed diam nonumy eirmod tempor invidunt ut labore et dolore magna aliquyam erat, sed diam voluptua. At vero eos et</p></div>
    <div class="feature" style="top:1052px"><span class="ic"></span><h3>We Make Clean &amp; Healthy Environment</h3><p class="small">Lorem ipsum dolor sit amet, consetetur sadipscing elitr, sed diam nonumy eirmod tempor invidunt ut labore et dolore magna aliquyam erat, sed diam voluptua. At vero eos et</p></div>
    <div class="feature" style="top:1133px"><span class="ic"></span><h3>We Are Highly Trained &amp; Professionals</h3><p class="small">Lorem ipsum dolor sit amet, consetetur sadipscing elitr, sed diam nonumy eirmod tempor invidunt ut labore et dolore magna aliquyam erat, sed diam voluptua. At vero eos et</p></div>
    <div class="photo why-photo" role="img" aria-label="Technician in protective suit standing beside a service van"></div>
  </section>

  <section class="srv">
    <div class="tag" style="left:520px;top:1342px">Commercial premises</div>
    <h2>Lorem ipsum dolor sit amet, consetetur sadipscing elitr, sed diam nonumy</h2>
    <div class="btn" style="left:520px;top:1431px;width:91px;height:28px">Book Now</div>

    <div class="svc" style="left:56px;top:1383px"><svg width="90" height="90" viewBox="0 0 90 90"><circle cx="42" cy="46" r="36" fill="#dff3e8"/><circle cx="47" cy="42" r="38" fill="none" stroke="#0f3f4a" stroke-width="4"/><circle cx="47" cy="42" r="30" fill="none" stroke="#0f3f4a" stroke-dasharray="3 3"/><path d="M22 17 72 67" stroke="#0f3f4a" stroke-width="4"/></svg><h3>Rodent Control</h3><p class="small">Lorem ipsum dolor sit amet, consetetur sadipscing elitr, sed diam nonumy eirmod tempor invidunt ut labore et dolore magna aliquyam</p></div>
    <div class="svc" style="left:277px;top:1441px"><svg width="90" height="90" viewBox="0 0 90 90"><circle cx="42" cy="46" r="36" fill="#dff3e8"/><circle cx="47" cy="42" r="38" fill="none" stroke="#0f3f4a" stroke-width="4"/><circle cx="47" cy="42" r="30" fill="none" stroke="#0f3f4a" stroke-dasharray="3 3"/><rect x="35" y="28" width="24" height="28" rx="3" fill="none" stroke="#0f3f4a" stroke-width="3"/></svg><h3>Stored Product Pest Control</h3><p class="small">Lorem ipsum dolor sit amet, consetetur sadipscing elitr, sed diam nonumy eirmod tempor invidunt ut labore et dolore magna aliquyam</p></div>
    <div class="svc" style="left:497px;top:1498px"><svg width="90" height="90" viewBox="0 0 90 90"><circle cx="42" cy="46" r="36" fill="#dff3e8"/><circle cx="47" cy="42" r="38" fill="none" stroke="#0f3f4a" stroke-width="4"/><circle cx="47" cy="42" r="30" fill="none" stroke="#0f3f4a" stroke-dasharray="3 3"/><path d="M22 17 72 67" stroke="#0f3f4a" stroke-width="4"/></svg><h3>Flying Insect Control</h3><p class="small">Lorem ipsum dolor sit amet, consetetur sadipscing elitr, sed diam nonumy eirmod tempor invidunt ut labore et dolore magna aliquyam</p></div>
    <div class="svc" style="left:56px;top:1650px"><svg width="90" height="90" viewBox="0 0 90 90"><circle cx="42" cy="46" r="36" fill="#dff3e8"/><circle cx="47" cy="42" r="38" fill="none" stroke="#0f3f4a" stroke-width="4"/><circle cx="47" cy="42" r="30" fill="none" stroke="#0f3f4a" stroke-dasharray="3 3"/><path d="M22 17 72 67" stroke="#0f3f4a" stroke-width="4"/></svg><h3>Spider And Insect Control</h3><p class="small">Lorem ipsum dolor sit amet, consetetur sadipscing elitr, sed diam nonumy eirmod tempor invidunt ut labore et dolore magna aliquyam</p></div>
    <div class="svc" style="left:277px;top:1709px"><svg width="90" height="90" viewBox="0 0 90 90"><circle cx="42" cy="46" r="36" fill="#dff3e8"/><circle cx="47" cy="42" r="38" fill="none" stroke="#0f3f4a" stroke-width="4"/><circle cx="47" cy="42" r="30" fill="none" stroke="#0f3f4a" stroke-dasharray="3 3"/><path d="M22 17 72 67" stroke="#0f3f4a" stroke-width="4"/></svg><h3>Termite Inspections &amp; Treatments</h3><p class="small">Lorem ipsum dolor sit amet, consetetur sadipscing elitr, sed diam nonumy eirmod tempor invidunt ut labore et dolore magna aliquyam</p></div>
    <div class="svc" style="left:497px;top:1767px"><svg width="90" height="90" viewBox="0 0 90 90"><circle cx="42" cy="46" r="36" fill="#dff3e8"/><circle cx="47" cy="42" r="38" fill="none" stroke="#0f3f4a" stroke-width="4"/><circle cx="47" cy="42" r="30" fill="none" stroke="#0f3f4a" stroke-dasharray="3 3"/><path d="M22 17 72 67" stroke="#0f3f4a" stroke-width="4"/></svg><h3>Ant</h3><p class="small">Lorem ipsum dolor sit amet, consetetur sadipscing elitr, sed diam nonumy eirmod tempor invidunt ut labore et dolore magna aliquyam</p></div>
  </section>

  <section class="facilities">
    <div class="tag" style="left:333px;top:2130px">Facilities we serve</div>
    <h2 class="h-sec" style="top:2161px">Lorem ipsum dolor sit amet, consetetur sadipscing elitr,<br>sed diam nonumy</h2>

    <article class="fac" style="top:2228px">
      <div class="photo" style="left:0;background:linear-gradient(135deg,#7a4d30,#b48a68 45%,#e8e2dc)" role="img" aria-label="Technician in protective suit spraying a kitchen bench"></div>
      <div class="body" style="left:352px">
        <svg width="30" height="30" viewBox="0 0 30 30"><path d="M6 14 15 6l9 8v11H6z" fill="none" stroke="#1d5a64" stroke-width="1.5"/><path d="M12 25v-6h6v6" fill="none" stroke="#1d5a64" stroke-width="1.5"/></svg>
        <h3>Residential</h3>
        <p class="small">Lorem ipsum dolor sit amet, consetetur sadipscing elitr, sed diam nonumy eirmod tempor invidunt ut labore et dolore magna aliquyam erat, sed diam voluptua. At vero eos et accusam et justo duo dolores et ea rebum. Stet clita kasd gubergren, no sea takimata sanctus.</p>
        <ul><li>Rodent</li><li>Termite inspections</li><li>Ant</li><li>Pre - purchase inspections</li><li>Spider</li><li>Termite treatments</li><li>Cockroach</li><li>Termite management systems</li><li>Termite control</li></ul>
        <div class="btn">Book Now</div>
      </div>
    </article>

    <article class="fac" style="top:2558px">
      <div class="photo" style="left:317px;background:linear-gradient(135deg,#5e4030,#a98a70 45%,#ece8e4)" role="img" aria-label="Technician kneeling and spraying under kitchen cabinets"></div>
      <div class="body" style="left:31px">
        <svg width="30" height="30" viewBox="0 0 30 30"><rect x="8" y="8" width="14" height="18" fill="none" stroke="#1d5a64" stroke-width="1.5"/><path d="M12 12h2M16 12h2M12 16h2M16 16h2" stroke="#1d5a64"/></svg>
        <h3>Commercial</h3>
        <p class="small">Lorem ipsum dolor sit amet, consetetur sadipscing elitr, sed diam nonumy eirmod tempor invidunt ut labore et dolore magna aliquyam erat, sed diam voluptua. At vero eos et accusam et justo duo dolores et ea rebum. Stet clita kasd gubergren, no sea takimata sanctus.</p>
        <ul><li>shopping centres</li><li>clubs</li><li>transport facilities</li><li>bars</li><li>restaurants</li><li>food</li><li>pubs</li><li>manufacturing facilities</li></ul>
        <div class="btn">Book Now</div>
      </div>
    </article>
  </section>

  <section class="abs stats">
    <h2>Let's See<br>Our Company<br>Life Statistics</h2>
    <div class="stat" style="left:336px"><b>500+</b><span>Satisfied clients</span></div>
    <div class="stat" style="left:445px"><b>1000+</b><span>Cases Resolved</span></div>
    <div class="stat" style="left:559px"><b>500+</b><span>Satisfied clients</span></div>
    <p class="small" style="color:#c7d8dc">Lorem ipsum dolor sit amet, consetetur sadipscing elitr, sed diam nonumy eirmod tempor invidunt ut labore et dolore magna.</p>
  </section>

  <section class="abs contact">
    <div class="abs appt" role="img" aria-label="Technician in protective suit behind a teal overlay">
      <div class="frame"></div>
      <svg class="abs" style="left:54px;top:48px" width="66" height="66" viewBox="0 0 66 66"><circle cx="33" cy="33" r="30" fill="#d9b23a"/><circle cx="33" cy="33" r="22" fill="none" stroke="#fff3c4" stroke-width="2"/></svg>
      <h3>Make An<br>Appointment</h3>
      <p class="small" style="color:#d6e6e8">Lorem ipsum dolor sit amet, consetetur sadipscing elitr, sed diam nonumy eirmod tempor invidunt ut labore et dolore magna aliquyam erat, sed diam voluptua. At vero eos et accusam et justo duo dolores et ea rebum.</p>
      <svg class="abs" style="left:46px;top:285px" width="26" height="10" viewBox="0 0 26 10"><path d="M0 5h24M20 1l4 4-4 4" stroke="#fff" fill="none"/></svg>
    </div>
    <h2>Contact Us</h2>
    <div class="field" style="top:62px">Your Name<svg width="10" height="10" viewBox="0 0 10 10"><circle cx="5" cy="3" r="2" fill="#8a97a0"/><path d="M1 10a4 4 0 0 1 8 0z" fill="#8a97a0"/></svg></div>
    <div class="field" style="top:101px">Your Email<svg width="10" height="10" viewBox="0 0 10 10"><rect x="1" y="2" width="8" height="6" fill="none" stroke="#8a97a0"/><path d="M1 2l4 3 4-3" fill="none" stroke="#8a97a0"/></svg></div>
    <div class="field" style="top:140px">Your Number<svg width="10" height="10" viewBox="0 0 10 10"><path d="M2 1l2 2-1 1.5 2.5 2.5L7 6l2 2-1.5 1.5C5 9 1 5 .5 2.5z" fill="#8a97a0"/></svg></div>
    <div class="field" style="top:179px;height:81px">Your Message<svg width="10" height="10" viewBox="0 0 10 10"><path d="M1 1h8v6H4L2 9V7H1z" fill="none" stroke="#8a97a0"/></svg></div>
    <div class="send">Send</div>
  </section>

  <footer class="abs footer">
    <div class="brand">Brightmoor Pest Services PTY LTD</div>
    <p class="about">Lorem ipsum dolor sit amet, consetetur sadipscing elitr, sed diam nonumy eirmod tempor invidunt ut labore et dolore magna aliquyam erat, sed diam voluptua. At vero eos et accusam et justo duo dolores et ea rebum.</p>
    <ul><li class="on">Home</li><li>About Us</li><li>Services</li><li>Facilities</li><li>Commercial</li><li>Residential</li></ul>
    <div class="ct">Contact Us</div>
    <div class="crow" style="top:76px"><i><svg width="6" height="8" viewBox="0 0 6 8"><path d="M3 8S0 4.5 0 3a3 3 0 0 1 6 0c0 1.5-3 5-3 5z" fill="#fff"/></svg></i><span>Lorem ipsum dolor sit amet,<br>consetetur sadipscing elitr,<br>Fairview, NSW 2150</span></div>
    <div class="crow" style="top:114px"><i><svg width="7" height="7" viewBox="0 0 10 10"><path d="M2 1l2 2-1 1.5 2.5 2.5L7 6l2 2-1.5 1.5C5 9 1 5 .5 2.5z" fill="#fff"/></svg></i><span style="padding-top:3px">(02) 5550 1847</span></div>
    <div class="crow" style="top:140px"><i><svg width="7" height="6" viewBox="0 0 10 8"><rect width="10" height="8" fill="#fff"/><path d="M0 0l5 4 5-4" fill="none" stroke="#262d52"/></svg></i><span style="padding-top:3px">hello@brightmoorpest.com.au</span></div>
    <div class="copy">© 2021 Brightmoor Pest Services PTY LTD. All rights reserved.</div>
  </footer>

</main>
</body>
</html>
```